New Alcoholic Spiked Seltzer Line

We need a can design for a line of low calorie alcoholic seltzer. This product is a sparkling water and vodka drink with no sugar added in a slim 12 oz can.

This is a lighter, healthier, alternative to the sugary ready-to-drinks on the market. The product contains only 3 ingredients: Vodka, Water and Natural Flavors. It has only 100 calories but still has 5% alcohol, so you don't need to sacrifice alcohol to cut calories.

This product also does not contain any preservatives.

We want this design to communicate the following objectives to the consumer and in this order:

1. Appetizing product
2.Low calorie
3.Communicate the type of beverage (Spiked Seltzer)

The brand name of the product is VELKA.

The flavor of the product needed to be used for the design is Mango-Orange.

Comparable products are:

www.brisavelfizz.example/
https://www.tarnowbubble.example
https://quellrind.example/

The designs should not infringe or copy the creative directions of the products mentionned above. They are only given so that you can better understand the type of product we are developing.

Target Market(s)

Young Professional women between the ages of 25 and 44

Industry/Entity Type

Product

Colors

Designer to choose colors to be used in the design.

Requirements
Must have
• Design extendibility, meaning it can be adapted for other flavors.
• This is a new category in the market we are targeting, so consumers must easily be able to identify what type of product this is.

```html
<!DOCTYPE html>
<html lang="en">
<head>
<meta charset="utf-8">
<title>VELKA Spiked Seltzer – Can Labels</title>
<link rel="stylesheet" href="https://fonts.googleapis.com/css2?family=Arimo:wght@400;700&family=Oswald:wght@400;700&display=swap">
<style>
  :root {
    --page: #ffffff;
    --frame: #9a9a9a;
    --can-body: #f5f7f7;
    --rim-light: #f2f2f2;
    --rim-dark: #c4c4c4;
    --ink: #000000;
    --mango: #f9a814;
    --orange: #ff6a05;
    --illustration: #d9dcdc;
  }
  html, body {
    margin: 0;
    padding: 0;
    width: 1200px;
    height: 1200px;
    overflow: hidden;
    background: var(--page);
  }
  .canvas {
    width: 1198px;
    height: 1198px;
    border: 1px solid var(--frame);
  }
  .canvas svg { display: block; }
  .can-body { fill: var(--can-body); }
  .can-rim { fill: url(#rimShade); }
  .scene-art { fill: var(--illustration); }
  .brand-name {
    font-family: "Oswald", sans-serif;
    font-weight: 700;
    font-size: 108px;
    fill: var(--ink);
  }
  .badge-pill { fill: var(--ink); }
  .badge-text {
    font-family: "Arimo", sans-serif;
    font-weight: 700;
    font-size: 19px;
    fill: #ffffff;
  }
  .flavor-name {
    font-family: "Oswald", sans-serif;
    font-weight: 400;
    font-size: 46px;
    letter-spacing: 2px;
    fill: var(--ink);
  }
  .abv {
    font-family: "Arimo", sans-serif;
    font-weight: 700;
    font-size: 24px;
    fill: var(--ink);
  }
  .calories {
    font-family: "Arimo", sans-serif;
    font-weight: 400;
    font-size: 22px;
    fill: var(--ink);
  }
  .divider { stroke: var(--ink); stroke-width: 1.5; }
  .splash-mango { fill: var(--mango); }
  .splash-orange { fill: var(--orange); }
</style>
</head>
<body>
<div class="canvas">
<svg width="1198" height="1198" viewBox="0 0 1198 1198" xmlns="http://www.w3.org/2000/svg">
  <defs>
    <linearGradient id="rimShade" x1="0" y1="0" x2="0" y2="1">
      <stop offset="0" stop-color="var(--rim-light)"/>
      <stop offset="1" stop-color="var(--rim-dark)"/>
    </linearGradient>
  </defs>

  <!-- Mango can -->
  <g class="can can--mango">
    <path class="can-rim" d="M82 186 Q320 50 558 186 L558 196 L82 196 Z"/>
    <path class="can-rim" d="M82 1054 L558 1054 L558 1066 Q540 1090 520 1100 Q320 1200 120 1100 Q100 1090 82 1066 Z"/>
    <path class="can-body" d="M82 196 Q320 76 558 196 L560 1056 Q320 1160 82 1056 Z"/>
    <rect class="scene-art" x="104" y="256" width="376" height="168" role="img" aria-label="Line drawing of a mountain range"/>
    <rect class="scene-art" x="118" y="432" width="294" height="124" role="img" aria-label="Line drawing of a hill with ski tracks"/>
    <rect class="scene-art" x="440" y="456" width="88" height="152" role="img" aria-label="Drawing of a pine tree"/>
    <path class="splash-mango" role="img" aria-label="Mango juice splash" d="M300 624 Q430 660 500 740 Q540 800 470 860 Q420 930 390 920 Q360 880 330 920 Q290 940 270 880 Q220 900 212 860 Q230 830 240 800 Q200 770 230 760 Q300 760 340 730 Q370 680 300 624 Z"/>
    <text class="brand-name" x="155" y="644">VELKA</text>
    <g transform="rotate(-22 186 722)">
      <rect class="badge-pill" x="110" y="706" width="152" height="32" rx="16"/>
      <text class="badge-text" x="186" y="729" text-anchor="middle">NO SUGAR</text>
    </g>
    <text class="flavor-name" x="360" y="835" text-anchor="middle">MANGO</text>
    <text class="abv" x="324" y="970" text-anchor="middle">5% alc/vol</text>
    <line class="divider" x1="224" y1="978" x2="420" y2="978"/>
    <text class="calories" x="322" y="1002" text-anchor="middle">ONLY 100 calories</text>
  </g>

  <!-- Orange can -->
  <g class="can can--orange" transform="translate(569 0)">
    <path class="can-rim" d="M82 186 Q320 50 558 186 L558 196 L82 196 Z"/>
    <path class="can-rim" d="M82 1054 L558 1054 L558 1066 Q540 1090 520 1100 Q320 1200 120 1100 Q100 1090 82 1066 Z"/>
    <path class="can-body" d="M82 196 Q320 76 558 196 L560 1056 Q320 1160 82 1056 Z"/>
    <rect class="scene-art" x="104" y="256" width="376" height="168" role="img" aria-label="Line drawing of a mountain range"/>
    <rect class="scene-art" x="118" y="432" width="294" height="124" role="img" aria-label="Line drawing of a hill with ski tracks"/>
    <rect class="scene-art" x="440" y="456" width="88" height="152" role="img" aria-label="Drawing of a pine tree"/>
    <path class="splash-orange" role="img" aria-label="Orange juice splash" d="M300 624 Q430 660 500 740 Q540 800 470 860 Q420 930 390 920 Q360 880 330 920 Q290 940 270 880 Q220 900 212 860 Q230 830 240 800 Q200 770 230 760 Q300 760 340 730 Q370 680 300 624 Z"/>
    <text class="brand-name" x="155" y="644">VELKA</text>
    <g transform="rotate(-22 186 722)">
      <rect class="badge-pill" x="110" y="706" width="152" height="32" rx="16"/>
      <text class="badge-text" x="186" y="729" text-anchor="middle">NO SUGAR</text>
    </g>
    <text class="flavor-name" x="360" y="835" text-anchor="middle">ORANGE</text>
    <text class="abv" x="324" y="970" text-anchor="middle">5% alc/vol</text>
    <line class="divider" x1="224" y1="978" x2="420" y2="978"/>
    <text class="calories" x="322" y="1002" text-anchor="middle">ONLY 100 calories</text>
  </g>
</svg>
</div>
</body>
</html>
```